New Business Card Design Project

We want a modern business card that catches the attention of other remodeling companies as well as homeowners. We would like it to be informative but still simple.

Target Market(s)

Residential and other Business's

Contact Information for Business Card

TrellBrix
Phone number is 5153927048
Address is
4817 SW 3rd Lane
Des Moines, Iowa 50313
email is trellbrixco@quamlet.com

Requirements
Must have
• Our tagline
• Honest | Professional | Affordable

```html
<!DOCTYPE html>
<html lang="en">
<head>
<meta charset="utf-8">
<title>TrellBrix Business Card</title>
<link rel="stylesheet" href="https://fonts.googleapis.com/css2?family=Open+Sans:wght@400;600;700;800&display=swap">
<style>
  :root {
    --page: #e4e4e4;
    --card: #232323;
    --card-soft: #2f2f2f;
    --blue: #2a66b8;
    --orange: #d4521f;
    --white: #f2f2f2;
  }
  * { margin: 0; padding: 0; box-sizing: border-box; }
  html, body { width: 1200px; height: 1021px; overflow: hidden; }
  body {
    background: var(--page);
    font-family: "Open Sans", sans-serif;
    position: relative;
  }
  .card {
    position: absolute;
    left: 290px;
    width: 620px;
    height: 354px;
    background: var(--card);
    overflow: hidden;
    box-shadow: 0 6px 18px rgba(0,0,0,.25);
  }
  .card--back { top: 88px; }
  .card--front { top: 540px; }

  .brand-name {
    font-weight: 800;
    color: var(--blue);
    letter-spacing: 2px;
    line-height: 1;
    text-transform: uppercase;
  }
  .tagline {
    font-weight: 700;
    color: var(--blue);
    letter-spacing: 1px;
    text-transform: uppercase;
    white-space: nowrap;
  }
  .tagline .sep { color: var(--orange); margin: 0 4px; }

  /* back */
  .back-mark {
    position: absolute;
    left: 70px; top: 90px;
    width: 210px; height: 210px;
    border-radius: 50%;
    background: var(--card-soft);
  }
  .card--back .brand {
    position: absolute;
    right: 40px; top: 210px;
    text-align: left;
  }
  .card--back .brand-name { font-size: 50px; }
  .card--back .tagline { font-size: 13px; margin-top: 6px; }

  /* front */
  .card--front .brand {
    position: absolute;
    left: 34px; top: 34px;
  }
  .card--front .brand-name { font-size: 52px; }
  .card--front .tagline { font-size: 13px; margin-top: 6px; }

  .divider {
    position: absolute;
    left: 34px; right: 40px; top: 178px;
    height: 1px;
    background: var(--orange);
  }
  .contact {
    position: absolute;
    left: 34px; top: 192px;
    list-style: none;
    color: var(--white);
    font-size: 15px;
    line-height: 1.45;
  }
  .contact li { display: flex; align-items: center; gap: 8px; }
  .contact svg { width: 14px; height: 14px; flex: none; }
  .person {
    position: absolute;
    right: 44px; top: 124px;
    text-align: right;
  }
  .person-name { color: var(--blue); font-size: 22px; font-weight: 600; }
  .person-role { color: var(--white); font-size: 15px; }

  .edge-band {
    position: absolute;
    left: 0; bottom: 0;
    width: 620px; height: 18px;
  }
</style>
</head>
<body>

  <section class="card card--back" aria-label="Business card back">
    <div class="back-mark"></div>
    <div class="brand">
      <div class="brand-name">TrellBrix</div>
      <div class="tagline">Honest<span class="sep">|</span>Professional<span class="sep">|</span>Affordable</div>
    </div>
  </section>

  <section class="card card--front" aria-label="Business card front">
    <div class="brand">
      <div class="brand-name">TrellBrix</div>
      <div class="tagline">Honest<span class="sep">|</span>Professional<span class="sep">|</span>Affordable</div>
    </div>

    <div class="person">
      <div class="person-name">Daniel Harper</div>
      <div class="person-role">Owner</div>
    </div>

    <div class="divider"></div>

    <ul class="contact">
      <li>4817 SW 3rd Lane</li>
      <li>Des Moines, IOWA 50313</li>
      <li>
        <svg viewBox="0 0 16 16" aria-hidden="true"><path fill="#d4521f" d="M3.6 1.5l2.3 2.6-1.3 1.8c.9 2 2.5 3.6 4.5 4.5l1.8-1.3 2.6 2.3-1.6 2.1C6.5 14.9 1.1 9.5.9 3.1z"/></svg>
        515-392-7048
      </li>
      <li>
        <svg viewBox="0 0 16 16" aria-hidden="true"><rect x="1" y="3" width="14" height="10" fill="none" stroke="#d4521f" stroke-width="1.5"/><path d="M1 3l7 6 7-6" fill="none" stroke="#d4521f" stroke-width="1.5"/></svg>
        trellbrixco@quamlet.com
      </li>
    </ul>

    <svg class="edge-band" viewBox="0 0 620 18" preserveAspectRatio="none" aria-hidden="true">
      <polygon points="0,0 382,0 370,18 0,18" fill="#2a66b8"/>
      <polygon points="382,0 388,0 376,18 370,18" fill="#111"/>
      <polygon points="388,0 620,0 620,18 376,18" fill="#d4521f"/>
    </svg>
  </section>

</body>
</html>
```